Innovative bakery bag design for “Dree Klinkhoff”

We are looking for an innovative, modern design for our new bakery bags.
The logo “Dree Klinkhoff – Coastal Oven Craft” will be used unchanged and in its original form.

The design should:

be clear and reduced, with high recognition value

preferably in black and white (e.g. white bag with black logo and subtle pattern/elements)

If colour is used, it should be used sparingly and stylishly (e.g. in our CI colours)

appear innovative and stand out from the classic bakery design

be simple but concise in design, with graphic elements that subtly underline our craftsmanship and regionality (e.g. heart symbol, grain pattern, Nordic elements, minimalist wavy line).

The design must work on white paper bags, optionally also on natural brown kraft paper bags. What is important is a high level of recognition and a modern, appealing aesthetic.

For inspiration: www.dreeklinkhoff.de or Insta: Dreeklinkhoff

```html
<!DOCTYPE html>
<html lang="en">
<head>
<meta charset="utf-8">
<title>Dree Klinkhoff – Bakery Bag</title>
<link rel="stylesheet" href="https://fonts.googleapis.com/css2?family=Cormorant+Garamond:wght@500&family=Montserrat:wght@400&display=swap">
<style>
  :root {
    --paper: #f1f0ee;
    --ink: #3b3636;
    --grain-top: #d9d5d2;
    --grain-mid: #9a9491;
    --grain-deep: #6f6966;
  }
  html, body {
    margin: 0;
    padding: 0;
    overflow: hidden;
  }
  body {
    width: 1200px;
    height: 1200px;
    background: var(--paper);
  }
  .bag-print {
    position: relative;
    width: 1200px;
    height: 1200px;
    background: var(--paper);
    overflow: hidden;
  }
  .brand-block {
    position: absolute;
    top: 330px;
    left: 0;
    width: 1200px;
    text-align: center;
    color: var(--ink);
  }
  .brand-name {
    margin: 0;
    font-family: "Cormorant Garamond", Georgia, serif;
    font-weight: 500;
    font-size: 120px;
    line-height: 1;
    letter-spacing: 0.02em;
  }
  .brand-tagline {
    margin: 26px 0 0;
    font-family: "Montserrat", Arial, sans-serif;
    font-weight: 400;
    font-size: 36px;
    line-height: 1;
    letter-spacing: 0.26em;
  }
  .grain-field {
    position: absolute;
    left: 0;
    bottom: 0;
    width: 1200px;
    height: 400px;
    display: block;
  }
</style>
</head>
<body>
  <main class="bag-print">
    <header class="brand-block">
      <h1 class="brand-name">Dree Klinkhoff</h1>
      <p class="brand-tagline">Coastal Oven Craft</p>
    </header>
    <svg class="grain-field" viewBox="0 0 1200 400" role="img" aria-label="Band of dark grey wheat ear illustrations rising at staggered heights from the bottom edge of the bag">
      <defs>
        <linearGradient id="grain-tone" x1="0" y1="0" x2="0" y2="1">
          <stop offset="0" stop-color="var(--grain-top)"/>
          <stop offset="0.45" stop-color="var(--grain-mid)"/>
          <stop offset="1" stop-color="var(--grain-deep)"/>
        </linearGradient>
      </defs>
      <path d="M0 20 C 80 10, 120 110, 200 90 S 320 30, 400 60 S 520 160, 620 140 S 760 60, 860 80 S 980 170, 1060 130 S 1160 20, 1200 10 L1200 400 L0 400 Z" fill="url(#grain-tone)"/>
    </svg>
  </main>
</body>
</html>
```